I need a design for a real estate multimedia company named Lumenfold Multimedia Services. We specialize in real estate photography, drone and all other forms for real estate media for the marketing of homes for sale.
I would like to see designs using the colors in my logo with some of my photography images (all attached) This will be for a 2005 Vantoria KLT (pic attached)

```html
<!DOCTYPE html>
<html lang="en">
<head>
<meta charset="utf-8">
<title>Lumenfold Multimedia Services — Vantoria KLT Wrap</title>
<link rel="stylesheet" href="https://fonts.googleapis.com/css2?family=Roboto:wght@900&display=swap">
<style>
  :root {
    --bg: #ffffff;
    --body: #f4f4f4;
    --body-edge: #cfcfcf;
    --brand-red: #d81e1e;
    --deep-red: #a8120f;
    --brand-yellow: #f2c81c;
    --navy: #14163d;
    --phone-grey: #9a9a9a;
    --sky: #6fa3e0;
    --house: #b89a7a;
    --stone: #6d6a66;
  }
  html, body {
    margin: 0;
    width: 1200px;
    height: 1012px;
    overflow: hidden;
    background: var(--bg);
  }
  .wrap-sheet { display: block; width: 1200px; height: 1012px; }
  .brand-name {
    font-family: "Roboto", sans-serif;
    font-weight: 900;
    fill: var(--navy);
  }
  .phone-number {
    font-family: "Roboto", sans-serif;
    font-weight: 900;
    fill: var(--phone-grey);
    letter-spacing: 1px;
  }
</style>
</head>
<body>
<svg class="wrap-sheet" viewBox="0 0 1200 1012" xmlns="http://www.w3.org/2000/svg">
  <defs>
    <linearGradient id="property-photo" x1="0" y1="0" x2="0" y2="1">
      <stop offset="0" stop-color="var(--sky)"/>
      <stop offset="0.3" stop-color="#d9cbb5"/>
      <stop offset="0.6" stop-color="var(--house)"/>
      <stop offset="1" stop-color="var(--stone)"/>
    </linearGradient>
    <linearGradient id="phone-band" x1="0" y1="0" x2="0" y2="1">
      <stop offset="0" stop-color="var(--brand-red)"/>
      <stop offset="1" stop-color="var(--deep-red)"/>
    </linearGradient>
    <clipPath id="panel-clip">
      <rect x="60" y="155" width="1090" height="240" rx="40"/>
    </clipPath>

    <g id="side-panel">
      <rect x="60" y="155" width="1090" height="240" rx="40" fill="var(--body)" stroke="var(--body-edge)" stroke-width="2"/>
      <g clip-path="url(#panel-clip)">
        <polygon class="photo-area" role="img" aria-label="Photograph of luxury homes with terraces, pool and stone stairs"
                 points="825,155 1150,155 1150,395 745,395" fill="url(#property-photo)"/>
        <polygon class="stripe-red-diagonal" points="822,155 838,155 758,395 742,395" fill="var(--brand-red)"/>
        <polygon class="stripe-red-thin" points="1008,155 1016,155 970,280 962,280" fill="var(--brand-red)"/>
        <polygon class="stripe-yellow-thin" points="1016,155 1022,155 976,280 970,280" fill="var(--brand-yellow)"/>
        <path class="stripe-yellow" d="M806,155 L766,300 Q760,318 740,318 L430,318 Q412,318 404,340 L392,380"
              fill="none" stroke="var(--brand-yellow)" stroke-width="14"/>
        <path class="phone-bar" d="M455,335 L735,335 Q748,335 744,350 L734,385 L440,385 Z" fill="url(#phone-band)"/>
        <polygon class="stripe-navy" points="398,318 412,318 378,395 360,395" fill="var(--navy)"/>
      </g>
    </g>
  </defs>

  <use href="#side-panel"/>
  <g class="brand-lockup">
    <text class="brand-name" x="590" y="262" font-size="48" text-anchor="middle">Lumenfold</text>
    <text class="brand-name" x="590" y="298" font-size="24" text-anchor="middle">Multimedia Services</text>
  </g>
  <text class="phone-number" x="595" y="376" font-size="36" text-anchor="middle">123-456-7890</text>

  <use href="#side-panel" transform="translate(1200,450) scale(-1,1)"/>
  <g class="brand-lockup">
    <text class="brand-name" x="650" y="712" font-size="48" text-anchor="middle">Lumenfold</text>
    <text class="brand-name" x="650" y="748" font-size="24" text-anchor="middle">Multimedia Services</text>
  </g>
  <text class="phone-number" x="605" y="826" font-size="36" text-anchor="middle">123-456-7890</text>
</svg>
</body>
</html>
```